KLT Business cards & stationary
Business cards and stationary
Project: KLT Business cards & stationary
KLT Business cards & stationary - Real Estate
Creative Brief
Use same font as used in my logo
Im not sure if my logo font will look good
Professional
Marcus Pellow
President
42 Tarrow Lane Suite 115 East Orange, NJ 07019
Marcus@marcusprealtyco.example
MarcusPrealtyco.example
company name on business card
marcusp marcusp
i definitely want to promote the website address on the card in a classy way also the company name should appear along with logo on the front

```html
<!DOCTYPE html>
<html lang="en">
<head>
<meta charset="utf-8">
<title>KLT Realty Co. — Business Cards</title>
<link rel="stylesheet" href="https://fonts.googleapis.com/css2?family=Cinzel:wght@600&family=Open+Sans:wght@400;600;700&display=swap">
<style>
  :root {
    --blue: #1f7dc2;
    --blue-deep: #1565a8;
    --blue-light: #3a97d6;
    --grey: #8c9196;
    --grey-light: #d9dcdf;
    --ink: #3c4146;
    --paper: #ffffff;
    --stage: #eceae6;
  }
  * { margin: 0; padding: 0; box-sizing: border-box; }
  html, body { width: 1200px; height: 904px; overflow: hidden; }
  body {
    background: var(--stage);
    font-family: "Open Sans", Arial, sans-serif;
    position: relative;
  }
  .card {
    position: absolute;
    width: 640px;
    height: 366px;
    border-radius: 4px;
    overflow: hidden;
    box-shadow: 0 10px 28px rgba(0,0,0,0.18);
  }

  /* Back of card */
  .card-back {
    left: 110px; top: 60px;
    background: linear-gradient(160deg, var(--blue-light), var(--blue) 55%, var(--blue-deep));
  }
  .card-back .mark {
    position: absolute; left: 0; right: 0; top: 110px;
    display: flex; align-items: center; justify-content: center; gap: 14px;
  }
  .mark-square {
    width: 58px; height: 58px;
    background: var(--paper);
    border-radius: 6px;
  }
  .card-back .mark-name {
    font-family: "Cinzel", Georgia, serif;
    font-weight: 600; font-size: 44px;
    color: var(--paper);
    letter-spacing: 3px;
  }
  .card-back .web {
    position: absolute; left: 0; right: 0; top: 218px;
    text-align: center;
    color: rgba(255,255,255,0.9);
    font-size: 15px; letter-spacing: 3px;
  }

  /* Front of card */
  .card-front {
    left: 450px; top: 478px;
    background: var(--paper);
  }
  .card-front .waves { position: absolute; left: 0; bottom: 0; }
  .brand {
    position: absolute; left: 40px; top: 110px;
    width: 260px;
    display: flex; flex-direction: column; align-items: center; gap: 16px;
  }
  .brand .mark-square { background: var(--blue); }
  .brand-name {
    font-family: "Cinzel", Georgia, serif;
    font-weight: 600; font-size: 30px;
    color: var(--blue);
    letter-spacing: 1px;
    white-space: nowrap;
  }
  .contact {
    position: absolute; left: 350px; top: 38px;
    color: var(--ink);
    font-size: 12.5px; line-height: 1.5;
  }
  .contact .name { color: var(--blue); font-weight: 700; font-size: 16px; line-height: 1.2; }
  .contact .title { font-size: 12px; color: var(--grey); margin-bottom: 12px; }
  .contact .address { margin-bottom: 14px; }
  .contact ul { list-style: none; }
  .contact li { display: flex; align-items: center; gap: 8px; }
  .contact li svg { width: 13px; height: 13px; flex: none; }
  .card-front .web {
    position: absolute; right: 34px; bottom: 22px;
    color: var(--paper);
    font-size: 14px; letter-spacing: 2px;
  }
</style>
</head>
<body>

  <section class="card card-back" aria-label="Card back">
    <div class="mark">
      <span class="mark-square"></span>
      <span class="mark-name">KLT</span>
    </div>
    <p class="web">MarcusPrealtyco.example</p>
  </section>

  <section class="card card-front" aria-label="Card front">
    <svg class="waves" width="640" height="366" viewBox="0 0 640 366" aria-hidden="true">
      <path d="M0 300 C 180 250, 360 300, 640 236 L640 252 C 380 312, 190 270, 0 318 Z" fill="var(--grey-light)"/>
      <path d="M0 318 C 190 270, 380 312, 640 252 L640 366 L0 366 Z" fill="var(--blue)"/>
      <path d="M0 312 C 200 262, 380 306, 640 244" fill="none" stroke="var(--grey)" stroke-width="1.5"/>
    </svg>

    <div class="brand">
      <span class="mark-square"></span>
      <span class="brand-name">KLT Realty Co.</span>
    </div>

    <div class="contact">
      <p class="name">Marcus Pellow</p>
      <p class="title">President</p>
      <p class="address">42 Tarrow Lane<br>Suite 115<br>Linden Falls, OR 97019</p>
      <ul>
        <li><svg viewBox="0 0 16 16"><path d="M4 1l3 3-2 2c1 2 3 4 5 5l2-2 3 3-2 3C7 15 1 9 1 3z" fill="var(--blue)"/></svg>555-014-2036</li>
        <li><svg viewBox="0 0 16 16"><rect x="4" y="1" width="8" height="14" rx="1.5" fill="var(--blue)"/><rect x="5.5" y="3" width="5" height="8" fill="#fff"/></svg>555-014-7719</li>
        <li><svg viewBox="0 0 16 16"><rect x="2" y="6" width="12" height="8" rx="1" fill="var(--blue)"/><rect x="4" y="2" width="8" height="5" fill="var(--grey)"/></svg>555-014-3358</li>
        <li><svg viewBox="0 0 16 16"><rect x="1" y="3" width="14" height="10" rx="1" fill="var(--blue)"/><path d="M1 4l7 5 7-5" fill="none" stroke="#fff" stroke-width="1.3"/></svg>Marcus@marcusprealtyco.example</li>
      </ul>
    </div>

    <p class="web">MarcusPrealtyco.example</p>
  </section>

</body>
</html>
```